Design business cards for Vantrelo

I am looking for a clean, crisp and professional business card design. A logo already exists with which to work, which is attached in various formats. The design needs to be print ready. A clear brief is attached - please read it carefully and ensure you can deliver what is required. Looking forward to awarding the prize to a great design and great designer!

```html
<!DOCTYPE html>
<html lang="en">
<head>
<meta charset="utf-8">
<title>Vantrelo Business Cards</title>
<link rel="stylesheet" href="https://fonts.googleapis.com/css2?family=Arimo:wght@400;700&display=swap">
<style>
  :root {
    --page-bg: #ecebe8;
    --card-bg: #ffffff;
    --ink-dark: #2f2f2f;
    --ink-grey: #5b5b5b;
    --brand-purple: #5b2a5f;
    --brand-orange: #e4793a;
    --icon-purple: #6a3a6e;
  }
  * { margin: 0; padding: 0; box-sizing: border-box; }
  html, body {
    width: 1200px; height: 912px; overflow: hidden;
    background: var(--page-bg);
    font-family: "Arimo", Arial, sans-serif;
  }
  .sheet { position: relative; width: 1200px; height: 912px; }
  .card {
    position: absolute; left: 250px; width: 700px; height: 400px;
    background: var(--card-bg);
    box-shadow: 0 2px 10px rgba(0,0,0,0.12);
  }
  .card--front { top: 41px; }
  .card--back { top: 471px; }

  .wordmark { position: absolute; display: flex; align-items: center; }
  .wordmark__dot { border-radius: 50%; background: var(--brand-purple); flex: none; }
  .wordmark__name { font-weight: 400; color: var(--ink-grey); letter-spacing: 1px; }

  .card--front .wordmark { left: 130px; top: 78px; gap: 18px; }
  .card--front .wordmark__dot { width: 58px; height: 58px; }
  .card--front .wordmark__name { font-size: 46px; }

  .holder { position: absolute; left: 70px; top: 262px; }
  .holder__name { font-size: 21px; font-weight: 700; color: var(--ink-dark); margin-bottom: 6px; }
  .holder__role { font-size: 14.5px; color: var(--brand-purple); line-height: 1.3; }

  .contacts { position: absolute; left: 400px; top: 176px; list-style: none; }
  .contacts li {
    display: flex; align-items: center; gap: 8px;
    font-size: 12.5px; color: var(--ink-grey); line-height: 20px;
  }
  .contacts .icon { width: 12px; height: 12px; flex: none; fill: var(--icon-purple); }
  .contacts .indent { padding-left: 20px; }

  .card--back .wordmark { left: 150px; top: 128px; gap: 24px; }
  .card--back .wordmark__dot { width: 92px; height: 92px; }
  .card--back .wordmark__name { font-size: 64px; }
  .tagline {
    position: absolute; right: 110px; top: 268px;
    font-size: 15px; color: var(--brand-purple);
  }
</style>
</head>
<body>
<main class="sheet">
  <section class="card card--front">
    <div class="wordmark">
      <span class="wordmark__dot"></span>
      <span class="wordmark__name">Vantrelo</span>
    </div>
    <div class="holder">
      <p class="holder__name">Adrian Calloway</p>
      <p class="holder__role">BE(Hons) PhD MIEAust GAICD<br>Director, Principal Consultant</p>
    </div>
    <ul class="contacts">
      <li><svg class="icon" viewBox="0 0 12 12"><path d="M2.5 1 L4.5 1 L5.2 3.6 L4 4.6 Q5 7 7.4 8 L8.4 6.8 L11 7.5 L11 9.5 Q10.5 11 9 11 Q1 10 1 3 Q1 1.5 2.5 1Z"/></svg>+61 (0)400 555 017</li>
      <li><svg class="icon" viewBox="0 0 12 12"><path d="M1 2.5 H11 V9.5 H1Z M1.6 3 L6 6.6 L10.4 3" fill="none" stroke="var(--icon-purple)" stroke-width="1.2"/></svg>acalloway@vantrelo.com.au</li>
      <li><svg class="icon" viewBox="0 0 12 12"><circle cx="6" cy="6" r="5"/></svg>adrian.calloway40</li>
      <li><svg class="icon" viewBox="0 0 12 12"><rect x="1" y="1" width="10" height="10" rx="2"/></svg>au.linkedin.com/in/acalloway</li>
      <li><svg class="icon" viewBox="0 0 12 12"><g fill="none" stroke="var(--icon-purple)" stroke-width="1.1"><circle cx="6" cy="6" r="4.8"/><ellipse cx="6" cy="6" rx="2.2" ry="4.8"/><path d="M1.2 6 H10.8"/></g></svg>www.vantrelo.com.au</li>
      <li><svg class="icon" viewBox="0 0 12 12"><path d="M6 1 L11 5.5 H9.5 V11 H7 V8 H5 V11 H2.5 V5.5 H1Z"/></svg>42 Marlow Street Kew East</li>
      <li class="indent">Victoria 3102 Australia</li>
    </ul>
  </section>

  <section class="card card--back">
    <div class="wordmark">
      <span class="wordmark__dot"></span>
      <span class="wordmark__name">Vantrelo</span>
    </div>
    <p class="tagline">“Design is the expression of intent”</p>
  </section>
</main>
</body>
</html>
```